Jewelry Shop Needs a Cash Coupon Design

Mabel’s Nook is a Hong Kong based fine jewelry brand. We need a Cash Coupon for marketing promotion use.
Size: 1/6 A4 Size (want to print 6 pieces in one A4 paper)
Font Content:
1. Company Logo
2. HKD 500
3. 现金券 Cash Voucher
4. Jewelry Willow Hall
5. 香港九龍油麻地平安街18-22號福林大廈5樓
5/F , Fairgrove Tower, 18-22 Ping On Street, YMT, HK
T: +852 29480517 F: +852 29480519 M: info@mabels-nook.example
Back Content:
1. Terms and Conditions
Mabel’s Nook philosophy is a jewelry icon of young, creative, trendy, fashionable, stylish, energetic, and elegant. For Mabel’s Nook, jewelry is one collection of artworks, the most important items in personal life.
Marketing

```html
<!DOCTYPE html>
<html lang="en">
<head>
<meta charset="utf-8">
<title>Mabel’s Nook – Cash Voucher Sheet</title>
<link rel="stylesheet" href="https://fonts.googleapis.com/css2?family=Cinzel:wght@400;500&family=UnifrakturMaguntia&family=Noto+Sans+TC:wght@400;500&display=swap">
<style>
  :root {
    --gold-edge: #7d6c14;
    --gold-mid: #c9b23a;
    --gold-light: #f2e77a;
    --ink: #141204;
    --divider: #5a5530;
    --silver-dark: #6f6f6f;
    --silver-light: #fbfbfb;
    --emblem: #050505;
  }
  * { margin: 0; padding: 0; box-sizing: border-box; }
  html, body { width: 848px; height: 1200px; overflow: hidden; background: var(--divider); }
  .sheet {
    width: 848px; height: 1200px;
    display: grid;
    grid-template-rows: repeat(6, 1fr);
    row-gap: 1px;
    background: var(--divider);
  }
  .voucher {
    position: relative;
    background:
      linear-gradient(180deg, rgba(255,255,255,0.08) 0%, rgba(0,0,0,0) 45%, rgba(60,45,0,0.18) 100%),
      linear-gradient(90deg, var(--gold-edge) 0%, var(--gold-mid) 18%, var(--gold-light) 42%, var(--gold-light) 55%, var(--gold-mid) 78%, var(--gold-edge) 100%);
    overflow: hidden;
  }
  .brand-emblem {
    position: absolute;
    left: 68px; top: 14px;
    width: 146px; height: 146px;
    border-radius: 50%;
    background: var(--emblem);
  }
  .brand-name {
    position: absolute;
    left: 8px; top: 160px;
    width: 268px;
    text-align: center;
    font-family: "Cinzel", serif;
    font-weight: 500;
    font-size: 23px;
    color: var(--ink);
    letter-spacing: 0.5px;
    white-space: nowrap;
  }
  .voucher-info {
    position: absolute;
    left: 390px; top: 18px;
    width: 450px;
    text-align: center;
    color: var(--ink);
  }
  .silver {
    background: linear-gradient(180deg, var(--silver-light) 0%, #c9c9c9 45%, var(--silver-dark) 100%);
    -webkit-background-clip: text;
    background-clip: text;
    color: transparent;
  }
  .house-name {
    font-family: "UnifrakturMaguntia", serif;
    font-size: 25px;
    line-height: 28px;
    padding-left: 40px;
    background: linear-gradient(180deg, #e8e8e8 0%, #8a8a8a 100%);
    -webkit-background-clip: text;
    background-clip: text;
    color: transparent;
  }
  .voucher-title {
    font-family: "Cinzel", serif;
    font-size: 33px;
    line-height: 42px;
    letter-spacing: 1px;
    white-space: nowrap;
  }
  .voucher-title .zh { font-family: "Noto Sans TC", sans-serif; font-size: 29px; letter-spacing: 0; }
  .voucher-value {
    font-family: "Cinzel", serif;
    font-size: 26px;
    line-height: 32px;
    padding-left: 44px;
  }
  .voucher-value .amount { color: var(--ink); font-family: "Noto Sans TC", sans-serif; font-weight: 400; }
  .address-zh {
    font-family: "Noto Sans TC", sans-serif;
    font-weight: 500;
    font-size: 13px;
    line-height: 19px;
    padding-left: 44px;
  }
  .address-en, .contact {
    font-family: "Cinzel", serif;
    font-size: 13.5px;
    line-height: 19px;
    white-space: nowrap;
  }
</style>
</head>
<body>
<main class="sheet">
  <section class="voucher">
    <div class="brand-emblem"></div>
    <div class="brand-name">Mabel’s Nook</div>
    <div class="voucher-info">
      <div class="house-name">Jewelry Willow Hall</div>
      <div class="voucher-title silver"><span class="zh">現金券</span> Cash Voucher</div>
      <div class="voucher-value"><span class="silver">HKD</span> <span class="amount">500</span></div>
      <div class="address-zh">香港九龍油麻地平安街18-22號福林大廈5樓</div>
      <div class="address-en">5/F , Fairgrove Tower, 18-22 Ping On Street, YMT, HK</div>
      <div class="contact">T: +852 29480517 F: +852 29480519 M: info@mabels-nook.example</div>
    </div>
  </section>
  <section class="voucher">
    <div class="brand-emblem"></div>
    <div class="brand-name">Mabel’s Nook</div>
    <div class="voucher-info">
      <div class="house-name">Jewelry Willow Hall</div>
      <div class="voucher-title silver"><span class="zh">現金券</span> Cash Voucher</div>
      <div class="voucher-value"><span class="silver">HKD</span> <span class="amount">500</span></div>
      <div class="address-zh">香港九龍油麻地平安街18-22號福林大廈5樓</div>
      <div class="address-en">5/F , Fairgrove Tower, 18-22 Ping On Street, YMT, HK</div>
      <div class="contact">T: +852 29480517 F: +852 29480519 M: info@mabels-nook.example</div>
    </div>
  </section>
  <section class="voucher">
    <div class="brand-emblem"></div>
    <div class="brand-name">Mabel’s Nook</div>
    <div class="voucher-info">
      <div class="house-name">Jewelry Willow Hall</div>
      <div class="voucher-title silver"><span class="zh">現金券</span> Cash Voucher</div>
      <div class="voucher-value"><span class="silver">HKD</span> <span class="amount">500</span></div>
      <div class="address-zh">香港九龍油麻地平安街18-22號福林大廈5樓</div>
      <div class="address-en">5/F , Fairgrove Tower, 18-22 Ping On Street, YMT, HK</div>
      <div class="contact">T: +852 29480517 F: +852 29480519 M: info@mabels-nook.example</div>
    </div>
  </section>
  <section class="voucher">
    <div class="brand-emblem"></div>
    <div class="brand-name">Mabel’s Nook</div>
    <div class="voucher-info">
      <div class="house-name">Jewelry Willow Hall</div>
      <div class="voucher-title silver"><span class="zh">現金券</span> Cash Voucher</div>
      <div class="voucher-value"><span class="silver">HKD</span> <span class="amount">500</span></div>
      <div class="address-zh">香港九龍油麻地平安街18-22號福林大廈5樓</div>
      <div class="address-en">5/F , Fairgrove Tower, 18-22 Ping On Street, YMT, HK</div>
      <div class="contact">T: +852 29480517 F: +852 29480519 M: info@mabels-nook.example</div>
    </div>
  </section>
  <section class="voucher">
    <div class="brand-emblem"></div>
    <div class="brand-name">Mabel’s Nook</div>
    <div class="voucher-info">
      <div class="house-name">Jewelry Willow Hall</div>
      <div class="voucher-title silver"><span class="zh">現金券</span> Cash Voucher</div>
      <div class="voucher-value"><span class="silver">HKD</span> <span class="amount">500</span></div>
      <div class="address-zh">香港九龍油麻地平安街18-22號福林大廈5樓</div>
      <div class="address-en">5/F , Fairgrove Tower, 18-22 Ping On Street, YMT, HK</div>
      <div class="contact">T: +852 29480517 F: +852 29480519 M: info@mabels-nook.example</div>
    </div>
  </section>
  <section class="voucher">
    <div class="brand-emblem"></div>
    <div class="brand-name">Mabel’s Nook</div>
    <div class="voucher-info">
      <div class="house-name">Jewelry Willow Hall</div>
      <div class="voucher-title silver"><span class="zh">現金券</span> Cash Voucher</div>
      <div class="voucher-value"><span class="silver">HKD</span> <span class="amount">500</span></div>
      <div class="address-zh">香港九龍油麻地平安街18-22號福林大廈5樓</div>
      <div class="address-en">5/F , Fairgrove Tower, 18-22 Ping On Street, YMT, HK</div>
      <div class="contact">T: +852 29480517 F: +852 29480519 M: info@mabels-nook.example</div>
    </div>
  </section>
</main>
</body>
</html>
```